Pediatric Pelvic Health Brochure

Looking to design a brochure for Marlow Brook's pelvic health program. I can provide imagery once I see the layout. Our website is marlowbrookpt.example so the look should reflect that

If you see PDF titled blue and word doc you will see what we provided as thoguhts.

Target Market(s)

parents of children

Industry/Entity Type

Health And Wellness

Font styles to use
Serif

Requirements
Must have
• clear call outs - easy to read with copy,
Should not have
• not look bland or dated

```html
<!DOCTYPE html>
<html lang="en">
<head>
<meta charset="utf-8">
<title>Marlow Brook – Pediatric Pelvic Health Brochure</title>
<link rel="stylesheet" href="https://fonts.googleapis.com/css2?family=Cinzel:wght@700&family=Montserrat:ital,wght@0,400;0,600;1,400&display=swap">
<style>
  :root{
    --navy:#123a8c;
    --navy-deep:#0c2b6e;
    --cyan:#29a8e0;
    --cyan-light:#6fcdf2;
    --paper:#f3f4f6;
    --ink:#1d2a4a;
    --stage:#5a5e64;
    --photo-warm:#c9b8ae;
    --photo-cool:#b9cfe0;
    --pool:#6ec3e6;
  }
  *{box-sizing:border-box;margin:0;padding:0}
  html,body{width:1200px;height:1200px;overflow:hidden}
  body{background:var(--stage);font-family:"Montserrat",sans-serif;color:var(--ink);position:relative}
  .brochure{position:absolute;left:60px;width:1080px;height:520px;background:var(--paper);overflow:hidden;box-shadow:0 10px 30px rgba(0,0,0,.35)}
  .brochure--outside{top:40px}
  .brochure--inside{top:640px}
  .shapes{position:absolute;inset:0;width:1080px;height:520px}
  .fold{position:absolute;top:0;bottom:0;width:1px;background:rgba(0,0,0,.08)}
  .t{position:absolute;font-size:10px;line-height:1.5}
  .heading{font-family:"Cinzel",serif;font-weight:700;color:var(--navy);letter-spacing:.02em}
  .heading--light{color:#fff}
  .heading--cyan{color:var(--cyan-light)}
  .body-copy{font-size:9.6px;line-height:1.5;color:var(--ink)}
  .body-copy p+p{margin-top:6px}
  .on-navy{color:#fff}
  .dash{display:block;width:26px;height:3px;background:var(--cyan);margin:7px 0}
  .brand{position:absolute;display:flex;align-items:center;gap:8px}
  .brand__mark{width:22px;height:22px;background:var(--navy)}
  .brand__name{font-family:"Cinzel",serif;font-weight:700;color:var(--navy);font-size:22px;line-height:1}
  .brand__tag{display:block;font-size:6.5px;letter-spacing:.12em;color:var(--cyan);margin-top:3px}
  .contact{position:absolute;left:360px;width:360px;text-align:center;color:#fff;font-size:11px}
  .contact svg{display:block;margin:0 auto 3px}
  .pill{position:absolute;background:var(--cyan);color:#fff;border-radius:20px;font-size:11px;letter-spacing:.12em;text-align:center;padding:7px 0}
  .phone-band{position:absolute;display:flex;align-items:center;gap:10px;color:#fff;font-weight:600;font-size:26px;letter-spacing:.06em}
</style>
</head>
<body>

<!-- OUTSIDE SPREAD -->
<section class="brochure brochure--outside">
  <svg class="shapes" viewBox="0 0 1080 520" aria-hidden="false">
    <defs>
      <linearGradient id="photoNurse" x1="0" y1="0" x2="1" y2="1">
        <stop offset="0" stop-color="#e7eaee"/><stop offset="1" stop-color="var(--photo-warm)"/>
      </linearGradient>
      <linearGradient id="photoBall" x1="0" y1="0" x2="0" y2="1">
        <stop offset="0" stop-color="#e9edf1"/><stop offset="1" stop-color="#9fd3cf"/>
      </linearGradient>
      <linearGradient id="navyFade" x1="0" y1="0" x2="0" y2="1">
        <stop offset="0" stop-color="var(--navy)"/><stop offset="1" stop-color="var(--navy-deep)"/>
      </linearGradient>
    </defs>
    <!-- Panel A -->
    <path d="M0 110 H360 V270 Q200 320 0 285 Z" fill="url(#photoNurse)" role="img" aria-label="Photo of a smiling clinician holding a baby"/>
    <path d="M0 290 Q190 325 360 262 V285 Q190 345 0 305 Z" fill="var(--cyan)"/>
    <path d="M0 305 Q190 345 360 285 V520 H0 Z" fill="url(#navyFade)"/>
    <!-- Panel B -->
    <path d="M360 0 H720 V140 Q545 235 360 130 Z" fill="var(--cyan)"/>
    <path d="M360 0 H720 V128 Q545 222 360 118 Z" fill="url(#navyFade)"/>
    <path d="M360 305 Q545 355 720 300 V520 H360 Z" fill="url(#navyFade)"/>
    <circle cx="545" cy="305" r="64" fill="#fff"/>
    <circle cx="545" cy="305" r="60" fill="#e6ecef" stroke="var(--cyan)" stroke-width="2" role="img" aria-label="Street map showing the clinic location"/>
    <!-- Panel C -->
    <path d="M720 255 Q905 390 1080 245 V268 Q905 410 720 278 Z" fill="var(--cyan)"/>
    <path d="M720 278 Q905 410 1080 268 V520 H720 Z" fill="url(#navyFade)"/>
    <circle cx="905" cy="205" r="118" fill="#fff"/>
    <circle cx="905" cy="205" r="112" fill="url(#photoBall)" role="img" aria-label="Photo of a therapist guiding a child balancing on an exercise ball"/>
  </svg>
  <span class="fold" style="left:360px"></span>
  <span class="fold" style="left:720px"></span>

  <!-- Panel A text -->
  <h2 class="t heading" style="left:34px;top:26px;font-size:20px;line-height:1.1">PEDIATRIC<br>PELVIC HEALTH</h2>
  <p class="t" style="left:34px;top:78px;font-size:9px;color:var(--ink)">Treating Infants, Children &amp; Adolescents<br><span style="color:var(--cyan)">www.marlowbrookpt.example</span></p>
  <div class="t on-navy" style="left:34px;top:350px;width:300px">
    <h3 class="heading heading--cyan" style="font-size:22px">Thank You</h3>
    <span class="dash"></span>
    <p style="font-size:12px;font-style:italic">But wait, I have a question,</p>
    <p style="font-size:9.5px;margin-top:4px">Call us at 212-555-0148 or<br>visit us at marlowbrookpt.example</p>
    <p style="font-size:9px;margin-top:10px;font-style:italic">Marlow Brook Physical &amp; Aquatic Therapy<br>Dana Whitfield, PT</p>
  </div>

  <!-- Panel B text -->
  <div class="t on-navy" style="left:380px;top:26px;width:320px;text-align:center">
    <p class="heading heading--cyan" style="font-size:15px">WE OFFER A</p>
    <p style="font-size:12px;font-weight:600;color:var(--cyan-light)">FREE 15 MINUTE CONSULTATION</p>
    <p style="font-size:11px;font-style:italic;margin-top:2px">to help you determine if physical<br>therapy is right for you.</p>
  </div>
  <div class="brand" style="left:455px;top:198px">
    <span class="brand__mark"></span>
    <span><span class="brand__name" style="font-size:20px">Marlow Brook</span><span class="brand__tag">PHYSICAL AND AQUATIC THERAPY</span></span>
  </div>
  <div class="contact" style="top:380px">
    <svg width="12" height="14" viewBox="0 0 12 14"><path d="M6 0a5 5 0 0 0-5 5c0 4 5 9 5 9s5-5 5-9a5 5 0 0 0-5-5zm0 7a2 2 0 1 1 0-4 2 2 0 0 1 0 4z" fill="var(--cyan-light)"/></svg>
    <p>120 Harbor Lane Ground Floor<br>Brookfield, NY 10990</p>
  </div>
  <div class="contact" style="top:425px">
    <svg width="12" height="12" viewBox="0 0 12 12"><path d="M2.5 0.5l2 2.5-1.2 1.5c.8 1.7 2.3 3.2 4 4l1.5-1.2 2.5 2-1.2 2C5 11 1 7 .5 2.5z" fill="var(--cyan-light)"/></svg>
    <p>212-555-0148</p>
  </div>
  <div class="contact" style="top:455px">
    <svg width="14" height="10" viewBox="0 0 14 10"><rect x=".5" y=".5" width="13" height="9" fill="none" stroke="var(--cyan-light)"/><path d="M.5 .5l6.5 5 6.5-5" fill="none" stroke="var(--cyan-light)"/></svg>
    <p>hello@marlowbrookpt.example</p>
  </div>
  <div class="contact" style="top:485px">
    <svg width="12" height="12" viewBox="0 0 12 12"><circle cx="6" cy="6" r="5.5" fill="none" stroke="var(--cyan-light)"/><path d="M.5 6h11M6 .5c-3 3-3 8 0 11M6 .5c3 3 3 8 0 11" fill="none" stroke="var(--cyan-light)"/></svg>
    <p>www.marlowbrookpt.example</p>
  </div>

  <!-- Panel C text -->
  <div class="brand" style="left:768px;top:34px">
    <span class="brand__mark" style="width:28px;height:28px"></span>
    <span><span class="brand__name" style="font-size:28px">Marlow Brook</span><span class="brand__tag" style="font-size:7.5px">PHYSICAL AND AQUATIC THERAPY</span></span>
  </div>
  <div class="t on-navy" style="left:740px;top:345px;width:320px;text-align:center">
    <h2 class="heading heading--cyan" style="font-size:34px;line-height:1">RECOVER</h2>
    <p class="heading heading--light" style="font-size:16px;margin-top:2px">STRENGTH AND BALANCE</p>
    <span class="dash" style="margin:7px auto"></span>
    <p style="font-size:10.5px">Benchmark your physical health with The Balance Check and stay on track to live an active and pain free life.</p>
  </div>
  <p class="pill" style="left:795px;top:470px;width:220px">www.marlowbrookpt.example</p>
</section>

<!-- INSIDE SPREAD -->
<section class="brochure brochure--inside">
  <svg class="shapes" viewBox="0 0 1080 520">
    <defs>
      <linearGradient id="photoPlay" x1="0" y1="0" x2="1" y2="1">
        <stop offset="0" stop-color="#d9d2d6"/><stop offset="1" stop-color="var(--photo-warm)"/>
      </linearGradient>
      <linearGradient id="photoPool" x1="0" y1="0" x2="0" y2="1">
        <stop offset="0" stop-color="var(--pool)"/><stop offset=".75" stop-color="#bfe4f3"/><stop offset="1" stop-color="var(--paper)"/>
      </linearGradient>
      <linearGradient id="navyFade2" x1="0" y1="0" x2="0" y2="1">
        <stop offset="0" stop-color="var(--navy-deep)"/><stop offset="1" stop-color="var(--navy)"/>
      </linearGradient>
    </defs>
    <!-- Panel A -->
    <path d="M0 0 H360 V150 Q330 215 0 205 Z" fill="url(#photoPlay)" role="img" aria-label="Photo of a therapist playing with a young girl on the floor"/>
    <path d="M0 205 Q330 215 360 150 V175 Q335 235 0 222 Z" fill="var(--cyan)"/>
    <!-- Panel B -->
    <path d="M360 0 H720 V250 H360 V175 Q380 120 360 0 Z" fill="url(#photoPool)" role="img" aria-label="Photo of therapists and children doing aquatic therapy in an indoor pool"/>
    <!-- Panel C -->
    <rect x="720" y="0" width="360" height="520" fill="url(#navyFade2)"/>
    <!-- Bottom band -->
    <path d="M0 498 Q540 470 720 462 Q900 440 1080 415 V520 H0 Z" fill="var(--cyan)"/>
  </svg>
  <span class="fold" style="left:360px"></span>
  <span class="fold" style="left:720px"></span>

  <!-- Panel A text -->
  <div class="t" style="left:34px;top:262px;width:292px">
    <h3 class="heading" style="font-size:17px">WE PARTNER</h3>
    <p class="body-copy" style="margin-top:8px">Pelvic dysfunction problems in children in general, and in those with neurological pathologies even more, are markedly different from those in adults. Thus a therapist needs to work with parents, teachers and other healthcare professionals such as urologists, GI's, pediatric physical therapists, and psychologists to provide an integrated and comprehensive plan of care.</p>
  </div>
  <div class="brand" style="left:80px;top:440px">
    <span class="brand__mark"></span>
    <span><span class="brand__name">Marlow Brook</span><span class="brand__tag">PHYSICAL AND AQUATIC THERAPY</span></span>
  </div>

  <!-- Panel B text -->
  <div class="t" style="left:392px;top:262px;width:298px">
    <h3 class="heading" style="font-size:17px">WE SPECIALIZE</h3>
    <div class="body-copy" style="margin-top:8px">
      <p>All pelvic physical therapy treatments are always done with a physical therapist trained in pediatric pelvic floor issues, and always with your doctor's knowledge. Children are dressed and parents and guardians are present.</p>
      <p>During each session, your child or teen will work exclusively with one of our pelvic health physical therapists to help build strength, improve movement, and strengthen the skills and confidence needed to complete daily activities.</p>
    </div>
    <span class="dash"></span>
    <p style="font-size:10px;letter-spacing:.12em">www.marlowbrookpt.example</p>
  </div>

  <!-- Panel C text -->
  <div class="t on-navy" style="left:746px;top:24px;width:310px">
    <h3 class="heading heading--light" style="font-size:17px">WE HELP</h3>
    <div class="body-copy on-navy" style="margin-top:6px">
      <p>Although millions of children suffer from pelvic floor dysfunction, it often takes a long time to receive the right treatment.</p>
      <p>Typically, children are toilet trained by age 4. After age 4, bowel and bladder dysfunction is considered a major medical issue that affects the family unit.</p>
      <p>Pelvic problems in children greatly influence the quality of life, self-image, social interactions, participation in sports, etc. A pelvic physical therapist can help restore normality in bladder and bowel function and prevent the progression of problems that, if untreated, may be carried over into adult life.</p>
    </div>
    <h3 class="heading heading--light" style="font-size:17px;margin-top:14px;line-height:1.15">WE TREAT A RANGE<br>OF DIAGNOSES</h3>
    <span class="dash"></span>
    <p class="body-copy on-navy">Constipation, Increased urinary frequency, Decreased urinary frequency, Day-time incontinence, Night-time incontinence, Bed-wetting or enuresis, Giggle incontinence, Incontinence in the athletic female child or teenager, Waking up in the night to urinate or nocturia, Difficulty with urination, straining, slow flow, pain during or after urination, Reduced sensation of bladder or bowel fullness, Pain in the abdomen, bladder or lower back, Fecal incontinence, Treatment after pediatric pelvic surgeries</p>
  </div>
  <div class="phone-band" style="left:790px;top:462px">
    <svg width="22" height="22" viewBox="0 0 12 12"><path d="M2.5 0.5l2 2.5-1.2 1.5c.8 1.7 2.3 3.2 4 4l1.5-1.2 2.5 2-1.2 2C5 11 1 7 .5 2.5z" fill="#fff"/></svg>
    <span>212-555-0148</span>
  </div>
</section>

</body>
</html>
```